Design Business Cards & Letter Head

I would like to get a fresh, minimal design for business cards & letter head. Design has to be very simplistic, with just black color. Logo file is attached here.
Name of the company: Brookvane Orbitworks LLP
Nature of business: IT/Technology
Website: [login to view URL]

The business card shouldn't have any physical address, but the letter head will have it. Just place xxx for the address part.

I need PSD for the business card & MS-Word file for the letter head.

Thanks!

```html
<!DOCTYPE html>
<html lang="en">
<head>
<meta charset="utf-8">
<title>Brookvane Orbitworks LLP — Business Card</title>
<link rel="stylesheet" href="https://fonts.googleapis.com/css2?family=Open+Sans:wght@400;700&display=swap">
<style>
  :root {
    --backdrop: #e8e8e8;
    --card-light: #eeeeee;
    --card-dark: #1b1b1b;
    --ink: #000000;
    --paper: #ffffff;
    --text-muted: #d6d6d6;
  }
  * { margin: 0; padding: 0; box-sizing: border-box; }
  html, body {
    width: 1200px;
    height: 800px;
    overflow: hidden;
    background: var(--backdrop);
    font-family: "Open Sans", Arial, sans-serif;
  }
  .canvas {
    position: relative;
    width: 1200px;
    height: 800px;
  }
  .card {
    position: absolute;
    top: 272px;
    width: 404px;
    height: 261px;
  }

  /* Front */
  .card-front {
    left: 135px;
    background: var(--card-light);
    border: 4px solid var(--ink);
  }
  .brand-name {
    position: absolute;
    left: 0;
    right: 0;
    top: 125px;
    transform: translateY(-50%);
    text-align: center;
    font-size: 28px;
    font-weight: 400;
    color: var(--ink);
    letter-spacing: 1px;
    line-height: 1;
  }

  /* Back */
  .card-back {
    left: 637px;
    background: var(--card-dark);
    border: 4px solid var(--paper);
    color: var(--paper);
    text-align: center;
  }
  .card-back p { position: absolute; left: 0; right: 0; line-height: 1.2; }
  .person-name { top: 31px; font-size: 18px; font-weight: 700; }
  .person-role { top: 57px; font-size: 12px; color: var(--text-muted); }
  .company-name { top: 104px; font-size: 20px; font-weight: 400; }
  .company-field { top: 132px; font-size: 12.5px; color: var(--text-muted); }
  .contact-phone { top: 183px; font-size: 10px; color: var(--text-muted); }
  .contact-web { top: 198px; font-size: 10px; color: var(--text-muted); }
</style>
</head>
<body>
  <main class="canvas">
    <section class="card card-front" aria-label="Business card front">
      <p class="brand-name">Brookvane</p>
    </section>

    <section class="card card-back" aria-label="Business card back">
      <p class="person-name">Mara Ellison</p>
      <p class="person-role">CEO</p>
      <p class="company-name">Brookvane Orbitworks LLP</p>
      <p class="company-field">IT/Technology</p>
      <p class="contact-phone">+61 2 5550 1842</p>
      <p class="contact-web">www.brookvane-orbit.com</p>
    </section>
  </main>
</body>
</html>
```